Varnok Business Card

We are a security company in Central Aus, we supply guards, patrols, alarm monitoring, cash in transit, major event security.

I would like a modern card, possibly matte finish with gloss logo.... up for anything really

Our business colors are black white and blue.

on the back side of the card i was thinking having our logo just centered or our slogan ( "Securing Your Territory 24/7" )

Industry/Entity Type

Security

Contact Information for Business Card

Company Name: Varnok Security Service
My Name: Gregor Pellham
Position: Director
Mobil: 0491 738 205
Work: 89 612 347
Fax: 89 61 23 48
Email: greg.pellham@varnok-example.com.au
web: varnok-example.com.au
Address: 14 Quarry Road Alice Springs NT 0870

```html
<!DOCTYPE html>
<html lang="en">
<head>
<meta charset="utf-8">
<title>Varnok Security Service – Business Card</title>
<link rel="stylesheet" href="https://fonts.googleapis.com/css2?family=Michroma&family=Exo+2:wght@400;500&display=swap">
<style>
  :root {
    --bg: #e9e9e7;
    --card: #ffffff;
    --blue: #1f7fd4;
    --ink: #2b2b2b;
    --muted: #6b6b6b;
    --shadow: rgba(0, 0, 0, 0.18);
  }
  * { box-sizing: border-box; margin: 0; padding: 0; }
  html, body {
    width: 1057px;
    height: 1200px;
    overflow: hidden;
    background: var(--bg);
  }
  .sheet {
    width: 1057px;
    height: 1200px;
    display: flex;
    align-items: center;
    justify-content: center;
    gap: 64px;
  }
  .card {
    position: relative;
    width: 420px;
    height: 690px;
    background: var(--card);
    box-shadow: 0 14px 34px var(--shadow);
    overflow: hidden;
  }
  .brand-name {
    font-family: "Michroma", sans-serif;
    color: var(--blue);
    letter-spacing: 3px;
    text-transform: uppercase;
  }

  /* Front */
  .card-front .brand-name {
    position: absolute;
    top: 62px;
    right: 64px;
    font-size: 30px;
  }
  .accent-band {
    position: absolute;
    top: 0;
    right: 12px;
    width: 24px;
    height: 100%;
    background: var(--blue);
  }
  .details {
    position: absolute;
    top: 250px;
    right: 36px;
    width: 330px;
    display: flex;
    flex-direction: column;
    align-items: flex-end;
    font-family: "Exo 2", sans-serif;
    color: var(--ink);
    text-align: right;
  }
  .person-name {
    font-family: "Michroma", sans-serif;
    font-size: 22px;
    letter-spacing: 1px;
    text-transform: uppercase;
    margin-right: 20px;
  }
  .person-role {
    font-size: 12px;
    letter-spacing: 2px;
    text-transform: uppercase;
    color: var(--muted);
    margin-right: 20px;
    margin-top: 4px;
  }
  .detail-row {
    width: 100%;
    font-size: 15px;
    line-height: 1.35;
    padding: 6px 20px 5px 0;
    border-bottom: 1px solid var(--blue);
  }
  .detail-row:first-of-type { margin-top: 30px; }
  .detail-gap { margin-top: 20px; }

  /* Back */
  .card-back .brand-name {
    position: absolute;
    top: 300px;
    left: 0;
    width: 100%;
    text-align: center;
    font-size: 40px;
  }
  .web-line {
    position: absolute;
    left: 40px;
    right: 70px;
    bottom: 90px;
    display: flex;
    align-items: center;
    gap: 12px;
    padding-bottom: 8px;
    border-bottom: 1px solid var(--blue);
    font-family: "Exo 2", sans-serif;
    font-size: 15px;
    color: var(--ink);
  }
  .web-icon { width: 20px; height: 20px; flex: none; }
</style>
</head>
<body>
  <main class="sheet">
    <section class="card card-front" aria-label="Card front">
      <div class="brand-name">Varnok</div>
      <div class="accent-band"></div>
      <div class="details">
        <p class="person-name">Gregor Pellham</p>
        <p class="person-role">Director</p>
        <p class="detail-row">14 Quarry Road<br>Alice Springs NT 0870</p>
        <p class="detail-row detail-gap">M 0491 738 205</p>
        <p class="detail-row">W 89 612 347 &nbsp; F 89 61 23 48</p>
        <p class="detail-row">greg.pellham@varnok-example.com.au</p>
        <p class="detail-row">varnok-example.com.au</p>
      </div>
    </section>

    <section class="card card-back" aria-label="Card back">
      <div class="brand-name">Varnok</div>
      <div class="web-line">
        <svg class="web-icon" viewBox="0 0 20 20" aria-hidden="true">
          <circle cx="10" cy="10" r="10" fill="#1f7fd4"/>
          <g fill="none" stroke="#ffffff" stroke-width="1.1">
            <circle cx="10" cy="10" r="6"/>
            <ellipse cx="10" cy="10" rx="2.6" ry="6"/>
            <line x1="4" y1="10" x2="16" y2="10"/>
          </g>
        </svg>
        <span>varnok-example.com.au</span>
      </div>
    </section>
  </main>
</body>
</html>
```